Palmcrest Loop Tours Splashpage

This webpage will be a holding page until our website is complete. This page needs to be designed to advertise our tours in Honolulu, Hawaii. So it is important to have prices displayed and have a Hawaiian theme.

1. Warm colors - suggest reds?
2. Hawaiian flower incorporated in design

3. Display prices
Adult - single Journey - $20
Adult - 1 Day - $20 (this needs to be displayed as a special deal/price because full price is $25)
Adult - 2 days - $30

Seniors - (62+) 1 Day + 1 Day Free - $20

Children 5 - 17 yrs - 1 Day - $13
Children 5 - 17 yrs - 2 Days - $15
Under 5 Yrs - Free

There will be an online booking button (text on button should say "Book Online", so please make sure it is clear where they can purchase the tickets.

3. A photo of our branded double decker bus should be incorporate on the page.

4. Our Message "Welcome to Palmcrest Loop Tours. Our Open Top Bus ensures you have an unrivalled view of Honolulu and all that this great city has to offer. We pass all of the city’s main sites, offering fantastic photo opportunities along the way. Our tour takes around 90 minutes. You can get on and off the bus as often as you want. Your ticket is valid for one or two days. All departures have commentary in English. If it’s raining, we have a sliding roof to keep you dry. Step on-board and let us show you the best of Honolulu."

5. Some tour sites our tour visits are: Harbor's Arcade, Waikiki beach, Moanu Palace, Keowena Palace/King statue, Rodney's statue

Target Market(s)

We are catering to an international adult audience (ranging from 25 - 60 yrs of age) that handles vacation planning.

Please visit www.brindlecoachways.ee to get an idea of our style.

Requirements
Must have
• 1. prices displayed where they be viewed easily - There will be an online booking button so please make sure it is clear where they can purchase the tickets.

2. Adult - 1 Day - $20 (this needs to be displayed as a special deal/price because full price is $25)

3. Photo of our double decker bus

4. Hawaiian flower incorporated in design

5. Bright colors (make sure orange isn't the main background color) but not overwhelming

6. Logo on webpage
Nice to have
• 1. Images of our tour sites
2. Other Hawaiian images such as palm trees, Maile Lei, Sun with sunglasses, flower lei, parrot, Hawaiian sunsets
Should not have
• -Do not want any shade of orange as the main background color

```html
<!DOCTYPE html>
<html lang="en">
<head>
<meta charset="utf-8">
<title>Palmcrest Loop Tours</title>
<link href="https://fonts.googleapis.com/css2?family=Luckiest+Guy&family=PT+Sans+Narrow:wght@700&family=PT+Sans:wght@700&family=Cormorant+Garamond:ital,wght@1,600&family=Share+Tech&family=Alike&family=Anton&display=swap" rel="stylesheet">
<style>
  :root {
    --page: #1b1b1b;
    --page-top: #0c0c0c;
    --red: #e3140e;
    --red-deep: #b80d08;
    --red-band: rgba(170, 10, 8, 0.45);
    --yellow: #ffd400;
    --yellow-light: #fff27a;
    --white: #ffffff;
    --ink: #1a1a1a;
    --call-text: #4a0d0a;
    --sky: #e8eef2;
    --facade: #d8d2bc;
    --lawn: #5fae2e;
  }
  * { box-sizing: border-box; margin: 0; padding: 0; }
  html, body { width: 1200px; height: 905px; overflow: hidden; }
  body {
    background: linear-gradient(var(--page-top) 0 19px, var(--page) 19px);
    position: relative;
    font-family: "PT Sans", sans-serif;
  }
  .splash {
    position: absolute; left: 31px; top: 19px;
    width: 1138px; height: 812px; overflow: hidden;
  }
  .bus-photo {
    position: absolute; inset: 0;
    background:
      linear-gradient(180deg, var(--sky) 0%, var(--facade) 40%, #c9c1a6 55%, #4c8f26 72%, var(--lawn) 100%);
  }
  .panel { position: absolute; inset: 0; width: 100%; height: 100%; }
  .brand {
    position: absolute; left: 17px; top: 24px;
    font-family: "Luckiest Guy", cursive; font-size: 46px; line-height: 1;
    color: var(--yellow); letter-spacing: 1px; white-space: nowrap;
  }
  .call-label {
    position: absolute; left: 200px; top: 89px; width: 295px; height: 40px;
    border-radius: 12px; background: rgba(150, 8, 6, 0.55);
    font-family: "Share Tech", sans-serif; font-size: 25px; letter-spacing: 2px;
    color: var(--call-text); display: flex; align-items: center; justify-content: center;
  }
  .call-number {
    position: absolute; left: 106px; top: 134px;
    font-family: "PT Sans Narrow", sans-serif; font-size: 52px; color: var(--white);
    letter-spacing: 1px; line-height: 1.1;
  }
  .deal-title {
    position: absolute; left: 23px; top: 232px;
    font-family: "Cormorant Garamond", serif; font-style: italic; font-weight: 600;
    font-size: 48px; color: var(--white); letter-spacing: 2px;
  }
  .offer-badge {
    position: absolute; left: 272px; top: 203px; width: 122px; height: 122px;
    border-radius: 50%; background: var(--yellow); border: 3px solid var(--ink);
    display: flex; flex-direction: column; align-items: center; justify-content: center;
    font-family: "Anton", sans-serif; color: var(--ink); line-height: 0.95;
    transform: rotate(-8deg);
  }
  .offer-badge span { font-size: 28px; }
  .offer-badge span + span { font-size: 34px; }
  .price-group {
    position: absolute; left: 11px; list-style: none;
    background: var(--red-band); border-radius: 4px;
  }
  .price-group.adult { top: 303px; width: 266px; height: 99px; padding: 3px 0 0 22px; }
  .price-group.children { top: 480px; width: 312px; height: 92px; padding: 0 0 0 20px; background: none; }
  .price-row {
    display: flex; align-items: center; gap: 8px; height: 29.5px;
    font-size: 17px; color: var(--white);
    border-bottom: 1px dotted rgba(255, 190, 180, 0.55);
    width: max-content; padding-right: 8px;
  }
  .price-row:last-child { border-bottom: none; }
  .bus-icon { width: 15px; height: 16px; flex: none; }
  .seniors {
    position: absolute; left: 11px; top: 430px; width: 312px; height: 38px;
    background: var(--red-band); border-radius: 4px;
    display: flex; align-items: center; padding-left: 11px;
    font-family: "PT Sans Narrow", sans-serif; font-size: 18px; color: var(--white);
  }
  .book-button {
    position: absolute; left: 17px; top: 620px; width: 318px; height: 57px;
    display: flex; align-items: center; text-decoration: none;
  }
  .book-button .pill {
    position: absolute; left: 31px; right: 0; top: 3px; bottom: 0;
    border-radius: 10px;
    background: linear-gradient(180deg, var(--yellow-light) 0%, var(--yellow) 55%, #f2b800 100%);
    box-shadow: 0 3px 6px rgba(0,0,0,0.35);
    display: flex; align-items: center; padding-left: 50px;
    font-family: "Alike", serif; font-size: 32px; color: #3a3006;
  }
  .book-button .dot {
    position: absolute; left: 0; top: -2px; width: 62px; height: 62px; border-radius: 50%;
    background: radial-gradient(circle at 40% 35%, #fff38a, var(--yellow) 60%, #e0a800);
    z-index: 1;
  }
  .flower { position: absolute; border-radius: 50%; }
  .flower.gold { left: 316px; top: 551px; width: 76px; height: 76px; background: #f7c41a; }
  .flower.pink { left: 373px; top: 615px; width: 70px; height: 70px; background: #e8246a; }
  .flower.black { left: 432px; top: 664px; width: 64px; height: 64px; background: #111; }
  .flower.rose { left: 509px; top: 724px; width: 58px; height: 58px; background: #e0204e; }
</style>
</head>
<body>
<main class="splash">
  <div class="bus-photo" role="img" aria-label="Photo of the branded red open-top double decker tour bus on a palm-lined Honolulu street"></div>

  <svg class="panel" viewBox="0 0 1138 812" preserveAspectRatio="none" aria-hidden="true">
    <defs>
      <radialGradient id="redGlow" cx="30%" cy="40%" r="75%">
        <stop offset="0" stop-color="#f02a16"/>
        <stop offset="1" stop-color="#cf0f09"/>
      </radialGradient>
    </defs>
    <path d="M0 0 H745 C480 120 300 380 345 600 C380 720 520 790 690 812 H0 Z" fill="url(#redGlow)"/>
    <path d="M745 0 C480 120 300 380 345 600 C380 720 520 790 690 812" fill="none" stroke="#ffffff" stroke-width="7"/>
  </svg>

  <div class="brand">Palmcrest Loop Tours</div>
  <div class="call-label">Honolulu Call:</div>
  <div class="call-number">0078 612 4490</div>

  <div class="deal-title">Special deal:</div>
  <div class="offer-badge"><span>SPECIAL</span><span>OFFER!</span></div>

  <svg width="0" height="0" style="position:absolute" aria-hidden="true">
    <symbol id="bus" viewBox="0 0 15 16">
      <rect x="1" y="0" width="13" height="13" rx="2" fill="#2a0a08"/>
      <rect x="3" y="2" width="9" height="5" fill="#e3140e"/>
      <circle cx="4" cy="10" r="1.2" fill="#e3140e"/>
      <circle cx="11" cy="10" r="1.2" fill="#e3140e"/>
      <rect x="2" y="13" width="3" height="3" fill="#2a0a08"/>
      <rect x="10" y="13" width="3" height="3" fill="#2a0a08"/>
    </symbol>
  </svg>

  <ul class="price-group adult">
    <li class="price-row"><svg class="bus-icon"><use href="#bus"/></svg>Adult - single Journey - $20</li>
    <li class="price-row"><svg class="bus-icon"><use href="#bus"/></svg>Adult - 1 Day - $20</li>
    <li class="price-row"><svg class="bus-icon"><use href="#bus"/></svg>Adult - 2 days - $30</li>
  </ul>

  <div class="seniors">Seniors - (62+) 1 Day + 1 Day Free - $20</div>

  <ul class="price-group children">
    <li class="price-row"><svg class="bus-icon"><use href="#bus"/></svg>Children 5 - 17 yrs - 1 Day - $13</li>
    <li class="price-row"><svg class="bus-icon"><use href="#bus"/></svg>Children 5 - 17 yrs - 2 Days - $15</li>
    <li class="price-row"><svg class="bus-icon"><use href="#bus"/></svg>Under 5 Yrs - Free</li>
  </ul>

  <a class="book-button" href="#book">
    <span class="dot" aria-hidden="true"></span>
    <span class="pill">Book Online</span>
  </a>

  <div class="flower gold" role="img" aria-label="Yellow hibiscus flower"></div>
  <div class="flower pink" role="img" aria-label="Pink hibiscus flower"></div>
  <div class="flower black" role="img" aria-label="Black hibiscus flower"></div>
  <div class="flower rose" role="img" aria-label="Red hibiscus flower"></div>
</main>
</body>
</html>
```